Business card for Internet Marketing Consultant

Simple - need a nice business card design using the logo elements and colors. Keywords: Progressive, professional, stylish, minimalist. Please use the kr as part of the design.

Info for card:

Gareth Pennock
Internet Marketing Strategist
Phone: (555) 813-2064
Email: gareth@korvantareach.com
Address: 2156 N. Halvern Ave., Ste. 118
Brackenford, Nevada 89412

Website: www.korvantareach.com

Business

Sans Serif

```html
<!DOCTYPE html>
<html lang="en">
<head>
<meta charset="utf-8">
<title>Korvanta Reach – Business Card</title>
<link rel="stylesheet" href="https://fonts.googleapis.com/css2?family=Poppins:wght@300;400;600&display=swap">
<style>
  :root {
    --stage: #3a3a3a;
    --card: #2a2a2b;
    --frame: #d9d9d9;
    --ink-light: #f2f2f2;
    --ink-mid: #b9b9b9;
    --ink-soft: #8c8c8c;
    --brand-blue: #1f6fd1;
    --ornament: #9a9a9a;
  }
  * { box-sizing: border-box; margin: 0; padding: 0; }
  html, body { width: 1200px; height: 997px; overflow: hidden; }
  body {
    background: var(--stage);
    font-family: "Poppins", sans-serif;
    position: relative;
  }
  .card {
    position: absolute;
    background: var(--card);
    border: 6px solid var(--frame);
    color: var(--ink-light);
  }

  /* Front */
  .card-front {
    left: 60px; top: 300px; width: 560px; height: 320px;
    display: flex; flex-direction: column; align-items: center; justify-content: center;
  }
  .brand { display: flex; align-items: center; gap: 12px; }
  .brand-dot {
    width: 22px; height: 22px; border-radius: 50%;
    background: var(--brand-blue);
  }
  .brand-name {
    font-weight: 600; color: var(--brand-blue);
    font-size: 40px; letter-spacing: -0.5px; line-height: 1;
  }
  .tagline {
    margin-top: 8px; font-weight: 300; color: var(--ink-soft);
    font-size: 13px; letter-spacing: 4px; text-transform: uppercase;
  }
  .front-web {
    position: absolute; right: 24px; bottom: 20px;
    font-size: 12px; color: var(--ink-mid);
  }

  /* Back */
  .card-back {
    left: 700px; top: 150px; width: 420px; height: 700px;
    padding: 40px 44px;
    display: flex; flex-direction: column; align-items: center;
  }
  .person-name { font-weight: 600; font-size: 24px; }
  .person-role { font-weight: 300; font-size: 13px; color: var(--ink-mid); margin-top: 4px; }
  .rule { width: 100%; height: 1px; background: var(--ink-soft); margin-top: 20px; }
  .ornament {
    width: 130px; height: 10px; margin-top: 18px;
    background: var(--ornament); opacity: .45; border-radius: 5px;
  }
  .card-back .brand { margin-top: 54px; }
  .card-back .brand-name { font-size: 32px; }
  .card-back .tagline { font-size: 10.5px; letter-spacing: 3px; margin-top: 6px; }
  .contact { list-style: none; width: 100%; margin-top: 40px; }
  .contact li {
    display: flex; align-items: center; gap: 18px;
    font-size: 15px; color: var(--ink-mid); margin-bottom: 24px; line-height: 1.4;
  }
  .contact svg { width: 26px; height: 26px; flex: none; fill: var(--ink-mid); }
</style>
</head>
<body>

  <section class="card card-front" aria-label="Card front">
    <div class="brand">
      <span class="brand-dot"></span>
      <span class="brand-name">korvantareach</span>
    </div>
    <p class="tagline">Internet Marketing Strategies</p>
    <p class="front-web">www.korvantareach.com</p>
  </section>

  <section class="card card-back" aria-label="Card back">
    <h1 class="person-name">Gareth Pennock</h1>
    <p class="person-role">Internet Marketing Strategist</p>
    <div class="rule"></div>
    <div class="ornament" role="img" aria-label="Decorative scroll flourish"></div>

    <div class="brand">
      <span class="brand-dot"></span>
      <span class="brand-name">korvantareach</span>
    </div>
    <p class="tagline">Internet Marketing Strategies</p>

    <div class="rule"></div>
    <div class="ornament" role="img" aria-label="Decorative scroll flourish"></div>

    <ul class="contact">
      <li>
        <svg viewBox="0 0 24 24" aria-hidden="true"><path d="M3 8c0-2 2-3 9-3s9 1 9 3v2h-4V8.5c-1-.5-3-.7-5-.7s-4 .2-5 .7V10H3zM6 11h12l2 8H4zm6 2a2.5 2.5 0 1 0 0 5 2.5 2.5 0 0 0 0-5z"/></svg>
        (555) 813-2064
      </li>
      <li>
        <svg viewBox="0 0 24 24" aria-hidden="true"><path d="M2 6h20v12H2zm2 2v.4l8 5.2 8-5.2V8l-8 5z"/></svg>
        gareth@korvantareach.com
      </li>
      <li>
        <svg viewBox="0 0 24 24" aria-hidden="true"><path d="M12 2a10 10 0 1 0 0 20 10 10 0 0 0 0-20zm0 2a8 8 0 0 1 6.9 4H15l-2 2 1 3-2 2v3l-2-1v-3l-3-2 1-3-2-2A8 8 0 0 1 12 4z"/></svg>
        www.korvantareach.com
      </li>
      <li>
        <svg viewBox="0 0 24 24" aria-hidden="true"><path d="M12 2a7 7 0 0 0-7 7c0 5 7 13 7 13s7-8 7-13a7 7 0 0 0-7-7zm0 4a3 3 0 1 1 0 6 3 3 0 0 1 0-6z"/></svg>
        <span>2156 N. Halvern Ave., Ste. 118<br>Brackenford, Nevada 89412</span>
      </li>
    </ul>
  </section>

</body>
</html>
```